Photography and Videography - Tidewell Studios - New Business Card Design

Tidewell Studios is a photography and Videography Company started by creative couple Rory K and Lena P and based on the Sunshine Coast in Queensland, Australia.
We're quirky, creative and innovative people and would like a business card that keeps you looking for more than just a few seconds.
Design wise we would like a black or charcoal background with a bit of a funkier design than just a boring old rectangle shape. Perhaps curved on an edge.
Ideally we would like to be able to make a collage of all of our best photos on the reverse side of the card with the company name or logo and "catch you by the tidewell..." (possibly in italics) underneath it.
On the front of the business card we would like our company name -
"Tidewell Studios", our motto- "Bringing Ideas To Life..." (possibly in italics) and our contact information. The background should be a darker colour like black or charcoal.
We like the look of having contact company details and contact info to one side (right) and a black and white photo of Rory K and Lena P to the other side (left).
Thank you and Good Luck!
Industry/Entity Type
Business
Contact Information for Business Card
Business Name - Tidewell Studios
Slogan - Bring Ideas To life
Name - Rory K | Lena P
Description - Photography | Videography
Phone - 0452 867 213 | 0438 926 057
Email - tidewellstudios@mailbox-example.com.au
Website - www.tidewellstudios-example.com.au
Like us on Facebook (symbol)
Logo styles of interest
Pictorial/Combination Logo
Look and feel

```html
<!DOCTYPE html>
<html lang="en">
<head>
<meta charset="utf-8">
<title>Tidewell Studios – Business Card</title>
<link rel="stylesheet" href="https://fonts.googleapis.com/css2?family=Michroma&family=Gochi+Hand&family=Cousine&display=swap">
<style>
  :root {
    --page: #ffffff;
    --card: #000000;
    --red: #e8000b;
    --yellow: #ffd400;
    --bracket: #3a3a3a;
    --photo-light: #b9b5ac;
    --photo-dark: #2a2926;
  }
  * { margin: 0; padding: 0; box-sizing: border-box; }
  html, body {
    width: 1200px; height: 1000px; overflow: hidden;
    background: var(--page);
  }
  .canvas { position: relative; width: 1200px; height: 1000px; }
  .card-shape { position: absolute; inset: 0; }
  .studio-name {
    position: absolute; top: 196px; left: 180px; width: 835px;
    text-align: center;
    font-family: "Michroma", sans-serif; font-weight: 400;
    font-size: 40px; letter-spacing: 1px; color: var(--red);
    text-transform: uppercase;
  }
  .services {
    position: absolute; top: 256px; left: 180px; width: 835px;
    text-align: center;
    font-family: "Gochi Hand", cursive;
    font-size: 44px; color: var(--yellow);
  }
  .portrait {
    position: absolute; left: 426px; top: 350px; width: 349px; height: 350px;
    background: radial-gradient(ellipse at 55% 40%, var(--photo-light), #8a867d 55%, var(--photo-dark));
  }
  .frame-brackets { position: absolute; inset: 0; pointer-events: none; }
  .partners {
    position: absolute; top: 738px; left: 180px; width: 835px;
    text-align: center;
    font-family: "Michroma", sans-serif;
    font-size: 38px; color: var(--yellow);
    text-transform: uppercase; letter-spacing: 1px;
  }
  .partners .accent { color: var(--red); }
  .partners .divider {
    display: inline-block; width: 3px; height: 46px; margin: 0 10px -6px;
    background: var(--red);
  }
  .contact {
    position: absolute; top: 814px; left: 180px; width: 835px;
    text-align: center;
    font-family: "Cousine", monospace;
    font-size: 30px; line-height: 39px; color: var(--red);
    letter-spacing: 1px;
  }
  .contact .email { font-size: 27px; letter-spacing: 0; }
</style>
</head>
<body>
<main class="canvas">
  <svg class="card-shape" width="1200" height="1000" viewBox="0 0 1200 1000" aria-hidden="true">
    <path class="card-body" fill="var(--card)"
      d="M270 145 H398 V110 A80 80 0 0 1 478 30 H718 A80 80 0 0 1 798 110 V145 H925 A90 90 0 0 1 1015 235 V895 A90 90 0 0 1 925 985 H270 A90 90 0 0 1 180 895 V235 A90 90 0 0 1 270 145 Z"/>
    <path class="stitch-border" fill="none" stroke="var(--red)" stroke-width="6" stroke-dasharray="24 14"
      d="M270 163 H415 V110 A63 63 0 0 1 478 47 H718 A63 63 0 0 1 781 110 V163 H925 A72 72 0 0 1 997 235 V895 A72 72 0 0 1 925 967 H270 A72 72 0 0 1 198 895 V235 A72 72 0 0 1 270 163 Z"/>
  </svg>

  <h1 class="studio-name">Tidewell Studios</h1>
  <p class="services">Photography and Videography</p>

  <div class="portrait" role="img" aria-label="Black and white portrait of Rory K and Lena P"></div>
  <svg class="frame-brackets" width="1200" height="1000" viewBox="0 0 1200 1000" aria-hidden="true">
    <g fill="none" stroke="var(--bracket)" stroke-width="3">
      <path d="M515 330 H404 V442"/>
      <path d="M682 330 H794 V442"/>
      <path d="M404 608 V720 H515"/>
      <path d="M794 608 V720 H682"/>
    </g>
  </svg>

  <p class="partners">R<span class="accent">or</span>y K.<span class="divider"></span>L<span class="accent">en</span>a P.</p>

  <address class="contact">
    <div class="phones">0438.926.057 OR 0452.867.213</div>
    <div class="email">tidewellstudios@mailbox-example.com.au</div>
    <div class="web">tidewellstudios-example.com.au</div>
  </address>
</main>
</body>
</html>
```